Brave Roads Ahead: Holding Hope, Meeting Storms, Voicing Triumph

I want a modern and clean looking book cover. 5.25x8

Title
Brave Roads Ahead

Subtitle
Holding Hope, Meeting Storms, Voicing Triumph

I don’t just want a graphic, I want it to make sense. If it can just be the words and a textured looking background, I’ll be ok with that too. I just want it to look crisp, clean, modern.

I want the back to have my book blurb and bio attached with the pic that’s attached.

Target Market(s)

Self help

Requirements
Must have
• Modern, clean look, look professional, attract customers.

```html
<!DOCTYPE html>
<html lang="en">
<head>
<meta charset="utf-8">
<title>Brave Roads Ahead – Book Cover</title>
<link rel="stylesheet" href="https://fonts.googleapis.com/css2?family=Titillium+Web:ital,wght@0,400;0,700;0,900;1,700&family=Open+Sans:wght@400;600&family=Playfair+Display:wght@700&display=swap">
<style>
  :root {
    --page-bg: #eceef0;
    --teal: #35998a;
    --teal-deep: #0f4a44;
    --teal-mid: #1d6a61;
    --teal-soft: #2a8276;
    --white: #ffffff;
    --ink: #123f3a;
  }
  * { box-sizing: border-box; margin: 0; padding: 0; }
  html, body { width: 1200px; height: 800px; overflow: hidden; }
  body { background: var(--page-bg); position: relative; font-family: "Open Sans", sans-serif; }

  .cover {
    position: absolute; top: 80px; width: 420px; height: 640px;
    background: var(--teal); overflow: hidden;
    box-shadow: 0 10px 28px rgba(0,0,0,.12);
  }
  .cover--front { left: 110px; }
  .cover--back { left: 670px; }

  /* Front */
  .initial {
    position: absolute; left: 30px; top: 250px;
    font-family: "Playfair Display", serif; font-weight: 700;
    font-size: 330px; line-height: 1; color: var(--white);
  }
  .figure-placeholder {
    position: absolute; left: 62px; top: 258px; width: 28px; height: 60px;
    background: var(--teal-deep); border-radius: 14px 14px 4px 4px;
  }
  .echo {
    position: absolute; top: 318px; height: 152px; width: 230px;
    border-radius: 6px;
  }
  .echo--1 { left: 150px; background: var(--teal-soft); }
  .echo--2 { left: 166px; background: var(--teal-mid); }
  .echo--3 { left: 182px; background: var(--teal-deep); }
  .title {
    position: absolute; left: 196px; top: 318px; width: 210px;
    font-family: "Titillium Web", sans-serif; font-weight: 900;
    font-size: 50px; line-height: 0.98; color: var(--white);
    text-transform: uppercase; letter-spacing: 0.5px;
  }
  .rule {
    position: absolute; left: 150px; top: 478px; width: 252px; height: 2px;
    background: var(--teal-deep);
  }
  .subtitle {
    position: absolute; left: 150px; top: 486px; width: 256px;
    font-family: "Titillium Web", sans-serif; font-weight: 700;
    font-size: 13px; color: var(--teal-deep);
  }
  .author {
    position: absolute; left: 150px; top: 540px; width: 256px; text-align: center;
    font-family: "Titillium Web", sans-serif; font-weight: 900;
    font-size: 20px; color: var(--white);
  }

  /* Back */
  .back-title {
    position: absolute; left: 30px; top: 34px; width: 360px; text-align: center;
    font-family: "Titillium Web", sans-serif; font-style: italic; font-weight: 700;
    font-size: 20px; color: var(--white);
  }
  .blurb {
    position: absolute; left: 30px; top: 72px; width: 360px;
    font-size: 10px; line-height: 1.45; color: var(--white);
  }
  .portrait-placeholder {
    position: absolute; left: 40px; top: 250px; width: 130px; height: 320px;
    background: linear-gradient(180deg, #2b5f58 0%, #cfe8e2 60%, #9fc9c0 100%);
    border-radius: 40px 40px 6px 6px;
  }
  .bio-name {
    position: absolute; left: 190px; top: 262px; width: 200px; text-align: center;
    font-family: "Titillium Web", sans-serif; font-weight: 700;
    font-size: 17px; color: var(--white);
  }
  .bio {
    position: absolute; left: 190px; top: 296px; width: 200px;
    font-size: 10px; line-height: 1.5; color: var(--ink);
  }
</style>
</head>
<body>
  <section class="cover cover--front" aria-label="Front cover">
    <div class="initial" aria-hidden="true">B</div>
    <div class="figure-placeholder" role="img" aria-label="Small silhouette of the author standing on the letter"></div>
    <div class="echo echo--1"></div>
    <div class="echo echo--2"></div>
    <div class="echo echo--3"></div>
    <h1 class="title">Brave<br>Roads<br>Ahead</h1>
    <div class="rule"></div>
    <p class="subtitle">Holding Hope, Meeting Storms, Voicing Triumph</p>
    <p class="author">Marisa Holloway</p>
  </section>

  <section class="cover cover--back" aria-label="Back cover">
    <h2 class="back-title">Brave Roads Ahead</h2>
    <p class="blurb">Everyone has big dreams, yet many of us stall at the first sign of doubt. This book is a warm and honest guide for anyone who has ever felt stuck between who they are and who they hope to become. Through personal stories, simple steps and daily reflection, you will learn to hold on to hope, meet every storm with courage and speak your goals into being. Whether you are starting over or pushing forward, these pages give you the push you need to keep moving toward the life you were made to live.</p>
    <div class="portrait-placeholder" role="img" aria-label="Full-length photo of the author standing with hands on hips"></div>
    <h3 class="bio-name">Marisa Holloway</h3>
    <p class="bio">A speaker, teacher and mentor, she has spent more than fifteen years helping women and young people find their voice. She holds degrees in education and counseling and has led workshops in schools, churches and community centers across the region. Her message is simple: fear is real, but faith is stronger. When she is not writing or coaching, she enjoys cooking for friends, long walks by the river and quiet mornings with her husband and two daughters.</p>
  </section>
</body>
</html>
```